Bramwell Joinery Website

My client Bramwell Joinery is looking for a redesign for a Word Press Website. Their current site is at www.bramwelljoinery.example They are a custom cabinet company, but also create bathroom, living room, bar and entertainment and bedroom cabinets too. They would like a design that emulates the master craftsman work they do yet a contemporary style.

Their current site was designed using Flash elements.

Target Market(s)

Home owners and builders of high end homes

Industry/Entity Type

Entertainment

Font styles to use
Serif
Decorative

Requirements
Must have
• Must show their work and logo using a contemporary style.
Nice to have
• Sliders that showcase their projects.

```html
<!DOCTYPE html>
<html lang="en">
<head>
<meta charset="utf-8">
<title>Bramwell Joinery</title>
<link href="https://fonts.googleapis.com/css2?family=PT+Sans+Narrow:wght@400;700&family=Libre+Baskerville&family=Open+Sans:wght@400;600&display=swap" rel="stylesheet">
<style>
:root{
  --orange:#e07a3e;
  --orange-soft:rgba(226,122,62,.85);
  --nav:#4a4745;
  --ink:#2b2b2b;
  --muted:#7a7a7a;
  --green:#5a9a1e;
  --band:#ebebeb;
  --grid:#f4f4f4;
  --cream:#f6f3c4;
  --sage:#dde5dc;
  --stone:#e5e5e5;
  --footer:#1f1f1f;
}
*{margin:0;padding:0;box-sizing:border-box}
html,body{width:840px;height:1200px;overflow:hidden;background:#fff}
body{position:relative;font-family:'Open Sans',sans-serif;color:var(--ink)}
.abs{position:absolute}

/* hero */
.hero{left:0;top:0;width:840px;height:403px;background:linear-gradient(180deg,#b9b4ae 0%,#d8d3cc 45%,#ece9e4 80%,#f1efec 100%)}
.hero-photo{left:0;top:0;width:840px;height:403px;background:linear-gradient(90deg,#3e3b3a 0%,#7b7672 14%,#cfc9c2 30%,#d9d4cd 70%,#9e968d 88%,#dcd8d2 100%);opacity:.55}
.logo{left:90px;top:0;width:80px;height:78px;background:var(--orange);display:flex;flex-direction:column;align-items:center;justify-content:center;gap:4px}
.logo-dot{width:14px;height:14px;border-radius:50%;background:#fff}
.logo-name{color:#fff;font-family:'PT Sans Narrow',sans-serif;font-size:11px;text-align:center;line-height:1.1}
.nav{left:212px;top:28px;width:550px;height:34px;background:var(--nav);display:flex;align-items:center}
.nav a{color:#fff;text-decoration:none;font-family:'PT Sans Narrow',sans-serif;font-size:11px;padding:0 8px;height:34px;line-height:34px;white-space:nowrap}
.nav a.active{background:var(--orange);padding:0 10px}
.hero-title{left:226px;top:101px;width:378px;height:61px;background:var(--orange-soft);color:#fff;font-family:'PT Sans Narrow',sans-serif;font-weight:700;font-size:47px;letter-spacing:2px;text-align:center;line-height:61px}
.hero-sub{left:180px;top:173px;width:480px;text-align:center;font-family:'PT Sans Narrow',sans-serif;font-size:14px;line-height:19px;color:#222}
.hero-btn{left:366px;top:234px;width:98px;height:25px;border:1px solid var(--orange);border-radius:3px;color:var(--orange);font-family:'PT Sans Narrow',sans-serif;font-size:10.5px;text-align:center;line-height:23px}
.dots{top:281px;left:377px}

/* service cards */
.band{left:0;top:403px;width:840px;height:125px;background:var(--band)}
.card{top:309px;width:188px;height:187px;background:#fff;box-shadow:0 6px 10px rgba(0,0,0,.18)}
.card-img{height:94px}
.card h3{position:absolute;left:8px;top:104px;font-family:'PT Sans Narrow',sans-serif;font-weight:400;font-size:11.5px;color:var(--orange)}
.card h3::before{content:"";display:inline-block;border-left:4px solid var(--orange);border-top:3px solid transparent;border-bottom:3px solid transparent;margin-right:5px;vertical-align:1px}
.card p{position:absolute;left:12px;top:126px;width:162px;font-size:6.2px;line-height:10px;color:var(--muted)}
.card p a{color:var(--green);text-decoration:none}

/* feature grid */
.gridsec{left:0;top:528px;width:840px;height:453px;background-color:var(--grid);background-image:linear-gradient(#e9e9e9 1px,transparent 1px),linear-gradient(90deg,#e9e9e9 1px,transparent 1px);background-size:14px 14px}
.panel{left:109px;top:544px;width:633px;height:414px;background:#fff}
.craft-img{left:126px;top:557px;width:186px;height:280px;background:linear-gradient(160deg,#5d6a3a 0%,#3c3a36 40%,#8a6a48 80%,#b99066 100%)}
.craft-box{left:126px;top:837px;width:186px;height:109px;background:var(--stone);text-align:center}
.craft-box h4{margin:18px 12px 0;padding-bottom:8px;border-bottom:1px solid #cfcfcf;font-family:'Libre Baskerville',serif;font-weight:400;font-size:10px;letter-spacing:.5px}
.craft-box p{margin:12px 8px 0;font-size:6.6px;line-height:13px;color:#555}
.promo{left:332px;top:558px;width:186px;height:176px;background:var(--cream);text-align:center}
.promo h2{margin-top:24px;font-family:'Libre Baskerville',serif;font-weight:400;font-size:13.5px;line-height:19.5px;letter-spacing:.5px}
.promo-rule{position:absolute;left:32px;top:115px;width:122px;height:1px;background:#aaa}
.promo-btn{position:absolute;left:26px;top:138px;width:136px;height:28px;border:1px solid #333;font-family:'PT Sans Narrow',sans-serif;font-size:11.5px;line-height:26px}
.doors-img{left:332px;top:754px;width:186px;height:192px;background:linear-gradient(170deg,#6b5644 0%,#c69e72 45%,#e2c79e 70%,#8a6e54 100%)}
.doors-tag{left:332px;top:900px;width:158px;height:27px;background:rgba(40,36,32,.75);color:#fff;font-family:'Libre Baskerville',serif;font-size:10px;line-height:27px;padding-left:10px}
.room-img{left:541px;top:558px;width:186px;height:192px;background:linear-gradient(160deg,#d9904a 0%,#e7a25a 40%,#f1ece0 65%,#6f7a52 100%)}
.room-box{left:541px;top:750px;width:186px;height:196px;background:var(--sage);text-align:center}
.room-box h4{margin-top:21px;font-family:'Libre Baskerville',serif;font-weight:400;font-size:10px;line-height:14px}
.room-box p{margin:12px 16px 0;font-size:6.6px;line-height:13px;color:#555}
.room-btn{position:absolute;left:50px;top:131px;width:98px;height:23px;border:1px solid #444;font-size:7.5px;line-height:21px}

/* footer */
.footer{left:0;top:981px;width:840px;height:216px;background:var(--footer);color:#e6e6e6}
.footer h5{position:absolute;top:20px;font-family:'PT Sans Narrow',sans-serif;font-weight:400;font-size:12.5px}
.footer p,.footer li{font-size:7px;line-height:10.7px}
.who{left:110px;top:54px;width:170px}
.more{position:absolute;left:230px;top:108px;font-size:7px;color:var(--orange)}
.links{position:absolute;left:338px;top:54px;list-style:none}
.links li{margin-bottom:2.7px}
.links li::before{content:"›";color:#aaa;margin-right:8px}
.links li.cur{color:var(--orange)}
.contact{left:557px;top:52px;width:160px}
.contact .row{position:absolute;left:0;display:flex;gap:8px}
.rule{left:110px;top:156px;width:632px;height:1px;background:#555}
.copy{left:110px;top:169px;font-size:7px}
.social{left:301px;top:166px;display:flex;gap:3px}
.social span{width:15px;height:15px;border-radius:50%}
.up{left:790px;top:141px;width:24px;height:24px;background:#8e8e8e}
.bottom{left:0;top:1197px;width:840px;height:3px;background:#eee}
</style>
</head>
<body>

<header>
  <div class="abs hero"></div>
  <div class="abs hero-photo" role="img" aria-label="Modern bathroom interior with dark cabinets and tiled walls"></div>
  <div class="abs logo"><span class="logo-dot"></span><span class="logo-name">Bramwell<br>Joinery</span></div>
  <nav class="abs nav">
    <a class="active" href="#">Home</a><a href="#">About us</a><a href="#">Gettomg Started</a><a href="#">Contact us</a><a href="#">Customer Experience</a><a href="#">Professional</a><a href="#">Portfolio</a><a href="#">Cabinet Hardware</a>
  </nav>
  <h1 class="abs hero-title">MORDEN BATH</h1>
  <p class="abs hero-sub">we've been designing and manufacturing the Midwest's finest<br>custom cabinets and fixtures.</p>
  <div class="abs hero-btn">View Designs</div>
  <svg class="abs dots" width="80" height="14" viewBox="0 0 80 14">
    <circle cx="8" cy="7" r="7" fill="none" stroke="#e07a3e" stroke-width="1"/>
    <circle cx="8" cy="7" r="1.5" fill="#e07a3e"/>
    <circle cx="29" cy="7" r="1.5" fill="#e07a3e"/>
    <circle cx="50" cy="7" r="1.5" fill="#e07a3e"/>
    <circle cx="69" cy="7" r="1.5" fill="#e07a3e"/>
  </svg>
</header>

<section>
  <div class="abs band"></div>
  <article class="abs card" style="left:109px">
    <div class="card-img" role="img" aria-label="White kitchen cabinets with island" style="background:linear-gradient(160deg,#6a5e52,#d8d2c8 50%,#8c7a66)"></div>
    <h3>Kitchens Cabinets</h3>
    <p>Lorem Ipsum is simply dummy text of the printing and typesetting industry. Lorem Ipsum has been the industry's standard dummy text ever since the 1500s. <a href="#">Read More...</a></p>
  </article>
  <article class="abs card" style="left:330px">
    <div class="card-img" role="img" aria-label="Living room with wall entertainment unit" style="background:linear-gradient(160deg,#d6d3cf,#f2f0ed 45%,#6c5a4c 90%)"></div>
    <h3>Living Room Cabinets</h3>
    <p>Lorem Ipsum is simply dummy text of the printing and typesetting industry. Lorem Ipsum has been the industry's standard dummy text ever since the 1500s. <a href="#">Read More...</a></p>
  </article>
  <article class="abs card" style="left:554px">
    <div class="card-img" role="img" aria-label="Bathroom with green wall and white vanity" style="background:linear-gradient(90deg,#eef0ea,#5aa02c 45%,#3f8a1e 75%,#f0f0ee)"></div>
    <h3>Bath Cabinets</h3>
    <p>Lorem Ipsum is simply dummy text of the printing and typesetting industry. Lorem Ipsum has been the industry's standard dummy text ever since the 1500s. <a href="#">Read More...</a></p>
  </article>
</section>

<section>
  <div class="abs gridsec"></div>
  <div class="abs panel"></div>
  <div class="abs craft-img" role="img" aria-label="Craftsman hand-carving a wooden panel"></div>
  <div class="abs craft-box">
    <h4>EXPERIENCE CRAFTSMAN</h4>
    <p>Lorem Ipsum is simply dummy text of the printing and typesetting industry. Lorem Ipsum has been the industry's standard dummy text</p>
  </div>
  <div class="abs promo">
    <h2>DESIGNING<br>&amp;<br>MANUFACTURING<br>CABINETS</h2>
    <div class="promo-rule"></div>
    <div class="promo-btn">View Portfolio</div>
  </div>
  <div class="abs doors-img" role="img" aria-label="Hands measuring a wooden board on a workbench"></div>
  <div class="abs doors-tag">MAKE CABINET DOORS&nbsp;&nbsp;&#9656;</div>
  <div class="abs room-img" role="img" aria-label="Bedroom with orange wall and sheer curtain"></div>
  <div class="abs room-box">
    <h4>MORDEN LIVING<br>ROOM DESIGN</h4>
    <p>Lorem Ipsum is simply dummy text of the printing and typesetting industry. Lorem Ipsum has been the industry's standard dummy text. our expert artisans help turn the house you live in to the home you've always dreamed of.</p>
    <div class="room-btn">View Design Styles</div>
    <svg style="position:absolute;left:68px;top:166px" width="60" height="22" viewBox="0 0 60 22">
      <circle cx="11" cy="11" r="10" fill="none" stroke="#333" stroke-width=".8"/>
      <circle cx="11" cy="11" r="1.8" fill="#222"/>
      <circle cx="33" cy="11" r="1.8" fill="#222"/>
      <circle cx="51" cy="11" r="1.8" fill="#222"/>
    </svg>
  </div>
</section>

<footer class="abs footer">
  <h5 style="left:110px">Who we are</h5>
  <p class="abs who">Bramwell Joinery has long stood as one of the Midwest's most renowned makers of custom cabinets and fixtures. Our handcrafted, award-winning creations have been chosen by hundreds of noteworthy homebuilders.</p>
  <span class="more">Read More...</span>

  <h5 style="left:332px">Important link</h5>
  <ul class="links">
    <li class="cur">Home</li><li>Our Portfolio</li><li>Cabinate Hardware</li><li>Professional</li><li>Curtomer Experience</li><li>Contact us</li>
  </ul>

  <h5 style="left:557px">Contact us</h5>
  <div class="abs contact">
    <div class="row" style="top:0">
      <svg width="8" height="10" viewBox="0 0 8 10"><path d="M4 0a3.6 3.6 0 0 0-3.6 3.6C.4 6.3 4 10 4 10s3.6-3.7 3.6-6.4A3.6 3.6 0 0 0 4 0z" fill="#ddd"/><circle cx="4" cy="3.6" r="1.3" fill="#1f1f1f"/></svg>
      <p>Bramwell Joinery<br>Nora Halvorsen<br>4780 W. Larchmont Road<br>Elmford, MO 60000</p>
    </div>
    <div class="row" style="top:66px">
      <svg width="8" height="8" viewBox="0 0 8 8"><path d="M0 3c0-2 8-2 8 0v1H6V3H2v1H0zM1.5 4h5L8 8H0z" fill="#ddd"/></svg>
      <p>Phone: 555.014.2290<br>Fax: 555.014.7731</p>
    </div>
  </div>

  <div class="abs rule"></div>
  <p class="abs copy">All rights reserved by Bramwell Joinery © 2015.</p>
  <div class="abs social">
    <span style="background:#3b5aa0"></span><span style="background:#2ea4e0"></span><span style="background:#f2d21c"></span>
  </div>
  <div class="abs up">
    <svg width="24" height="24" viewBox="0 0 24 24"><path d="M12 6l6 7h-3.5v5h-5v-5H6z" fill="#fff"/></svg>
  </div>
</footer>
<div class="abs bottom"></div>

</body>
</html>
```